New business Card Design

I'm looking to do a new design for our business cards.

Our Company its called the Garden quarter we are a High end outdoor Design and construction company based out of miami FL

Our Style is elegant, minimalist, Luxury but accessible.

see our Website: www.thegardenquarter-example.com

Attached find our logo as well as some samples the cards that we have for our sister company.

Sample Contact information ( in no particular order):

Marco Ventresca
VP of Sales and Marketing
Marco@thegardenquarter-example.com
555.204.7719
4172 NW 63 AVE Miami Florida, 33199

Designs are Looking Great guys but not quite there yet!

Upload your last few designs between today and Tomorrow. we will be choosing one on Saturday!

Cheers, 

Marco Ventresca
Director Of Marketing 

Hello Guys, 

Sorry we have not made a decision yet.  a lot of cool stuff! just narrowing down our options. 
expect a decision with in a day or 2. 

Marco. 

Target Market(s)

high End Design and construction. Luxurious but accessible

Industry/Entity Type

Construction

Colors

Designer to choose colors to be used in the design.

```html
<!DOCTYPE html>
<html lang="en">
<head>
<meta charset="utf-8">
<title>The Garden Quarter – Business Card</title>
<link href="https://fonts.googleapis.com/css2?family=Questrial&display=swap" rel="stylesheet">
<style>
  :root {
    --page-bg: #e6e4e0;
    --navy: #123a63;
    --navy-deep: #0b2a4a;
    --brand-blue: #1f7fc4;
    --brand-green: #6cb33f;
    --text-dark: #3a3a3a;
    --text-mid: #555;
    --wordmark-light: #e4e9ef;
    --card-light: #ffffff;
    --card-shade: #e9e9e9;
  }
  * { box-sizing: border-box; margin: 0; padding: 0; }
  html, body { width: 1200px; height: 871px; overflow: hidden; }
  body {
    background: var(--page-bg);
    font-family: "Questrial", "Century Gothic", sans-serif;
    position: relative;
  }
  .card {
    position: absolute;
    width: 520px;
    height: 297px;
    top: 287px;
    border-radius: 2px;
    box-shadow: 0 6px 18px rgba(0,0,0,.22);
    overflow: hidden;
  }

  /* Back side */
  .card-back {
    left: 50px;
    background: radial-gradient(ellipse at 60% 30%, var(--navy) 0%, var(--navy-deep) 85%);
  }
  .card-back .wordmark {
    position: absolute;
    left: 240px; top: 130px;
    width: 260px;
    color: var(--wordmark-light);
    font-size: 19px;
    letter-spacing: 1px;
    text-transform: uppercase;
    white-space: nowrap;
  }

  /* Front side */
  .card-front {
    left: 630px;
    background: linear-gradient(120deg, var(--card-light) 35%, var(--card-shade) 100%);
  }
  .brand-block {
    position: absolute;
    left: 26px; top: 40px;
    width: 190px;
  }
  .brand-block .brand-dot {
    width: 150px; height: 150px;
    border-radius: 50%;
    background: var(--brand-blue);
  }
  .brand-block .brand-name {
    margin-top: 18px;
    color: var(--brand-blue);
    font-size: 15px;
    letter-spacing: 1px;
    text-transform: uppercase;
    white-space: nowrap;
  }
  .contact {
    position: absolute;
    right: 28px; top: 70px;
    width: 300px;
    text-align: right;
  }
  .contact .name {
    color: var(--text-dark);
    font-size: 15px;
    font-weight: 700;
    letter-spacing: 1.5px;
  }
  .contact .title {
    color: var(--brand-blue);
    font-size: 12px;
    letter-spacing: 1px;
    margin-top: 2px;
  }
  .contact .address {
    color: var(--text-mid);
    font-size: 10.5px;
    letter-spacing: .8px;
    margin-top: 14px;
  }
  .contact-lines {
    list-style: none;
    margin-top: 26px;
  }
  .contact-lines li {
    display: flex;
    justify-content: flex-end;
    align-items: center;
    gap: 12px;
    color: var(--text-mid);
    font-size: 10.5px;
    letter-spacing: .8px;
    height: 20px;
    white-space: nowrap;
  }
  .contact-lines svg { width: 11px; height: 11px; flex: none; }
</style>
</head>
<body>
  <section class="card card-back" aria-label="Card back">
    <p class="wordmark">The Garden Quarter</p>
  </section>

  <section class="card card-front" aria-label="Card front">
    <div class="brand-block">
      <div class="brand-dot"></div>
      <p class="brand-name">The Garden Quarter</p>
    </div>
    <div class="contact">
      <p class="name">Marco Ventresca</p>
      <p class="title">VP of Sales and Marketing</p>
      <p class="address">4172 NW 63 AVE Miami Florida, 33199</p>
      <ul class="contact-lines">
        <li>555.204.7719
          <svg viewBox="0 0 12 12" aria-hidden="true"><path d="M2 1.5h2.2l1 2.5-1.3 1a6 6 0 0 0 3 3l1-1.3 2.6 1V10a1.2 1.2 0 0 1-1.2 1.2A9 9 0 0 1 .8 2.7 1.2 1.2 0 0 1 2 1.5z" fill="var(--brand-green)"/></svg>
        </li>
        <li>Marco@thegardenquarter-example.com
          <svg viewBox="0 0 12 12" aria-hidden="true"><rect x="1" y="2.5" width="10" height="7" rx="1" fill="var(--brand-green)"/><path d="M1.5 3l4.5 3.5L10.5 3" stroke="#fff" stroke-width="1" fill="none"/></svg>
        </li>
        <li>www.thegardenquarter-example.com
          <svg viewBox="0 0 12 12" aria-hidden="true"><circle cx="6" cy="6" r="5" fill="var(--brand-green)"/><path d="M1 6h10M6 1c2.2 2.5 2.2 7.5 0 10M6 1c-2.2 2.5-2.2 7.5 0 10" stroke="#fff" stroke-width=".8" fill="none"/></svg>
        </li>
      </ul>
    </div>
  </section>
</body>
</html>
```